Bright And Steady Web Design & Marketing

Will award a 2nd place prize of $100.00 if someone can come up with a logo to match this design!
Updates

Okay, I'm really looking to see some better designs here. What do you think will bring the best designs out? Please remember with all future submissions I'm looking for a cartoon style / illustrator style website. I'm not sure what the technical term is for it, so I uploaded some images in the brief.

Target Market(s)

Small Business Owners

Industry/Entity Type

Marketing

Logo Text

BrightAndSteady.example

Number of Pages Required

1 page

Colors

Designer to choose colors to be used in the design.

Requirements
Must have
• Logo should say BrightAndSteady.example I would like more than just a text logo. I want some sort of cool custom graphic / icon with it that will look nice on shirts/hats/etc

```html
<!DOCTYPE html>
<html lang="en">
<head>
<meta charset="utf-8">
<title>Bright And Steady Web Design & Marketing</title>
<link rel="stylesheet" href="https://fonts.googleapis.com/css2?family=Montserrat:wght@400;600;700;800;900&family=Open+Sans:ital,wght@0,400;0,600;1,400&display=swap">
<style>
:root{
  --blue:#1ea7e1;
  --blue-dark:#1589bd;
  --navy:#0d1a29;
  --ink:#333;
  --muted:#777;
  --faint:#ececec;
  --light:#f3f3f3;
  --white:#fff;
}
*{box-sizing:border-box;margin:0;padding:0}
html,body{width:1200px;height:4891px;overflow:hidden}
body{position:relative;font-family:"Open Sans",Arial,sans-serif;color:var(--ink);background:var(--white)}
.section{position:absolute;left:0;width:1200px;overflow:hidden}
.abs{position:absolute}
.center{left:0;width:1200px;text-align:center}

/* header */
.hero{top:0;height:700px;background:radial-gradient(ellipse at 50% 70%,#2c3136 0%,#15181b 55%,#0a0b0d 100%)}
.hero-photo{position:absolute;left:0;top:0;width:1200px;height:700px;background:linear-gradient(180deg,rgba(0,0,0,.25),rgba(60,64,70,.25) 70%,rgba(180,185,190,.25))}
.site-logo{left:40px;top:30px;display:flex;align-items:center;gap:9px;color:var(--blue);font-family:"Montserrat",sans-serif;font-weight:700}
.site-logo .mark{width:30px;height:30px;border-radius:50%;background:var(--blue);flex:none}
.site-logo .word{font-size:15px;line-height:18px}
.site-logo .word small{display:block;font-size:9px;line-height:13px;letter-spacing:1px}
.nav{left:310px;top:40px;display:flex;gap:30px;font-family:"Montserrat",sans-serif;font-size:12px;color:#ddd;font-weight:600;white-space:nowrap}
.nav .active{color:var(--blue)}
.phone-btn{left:930px;top:28px;width:195px;height:44px;background:var(--blue);color:#fff;border-radius:3px;font-family:"Montserrat",sans-serif;font-weight:700;font-size:21px;display:flex;align-items:center;justify-content:center;gap:10px}
.hero-kicker{top:228px;font-family:"Montserrat",sans-serif;font-size:31px;font-weight:600;letter-spacing:9px;color:#fff}
.hero-title{top:286px;font-family:"Montserrat",sans-serif;font-size:55px;line-height:68px;font-weight:800;color:var(--blue)}
.hero-swoosh{left:555px;top:432px}
.btn-outline{left:508px;top:524px;width:184px;height:48px;border:2px solid var(--blue);border-radius:24px;color:#fff;font-family:"Montserrat",sans-serif;font-size:12px;font-weight:600;display:flex;align-items:center;justify-content:center}
.scroll{top:636px;color:#fff;font-family:"Montserrat",sans-serif;font-size:12px;letter-spacing:3px}

/* headings */
.ghost{font-family:"Montserrat",sans-serif;font-weight:900;font-size:62px;line-height:62px;color:var(--faint)}
.sub{font-family:"Montserrat",sans-serif;font-weight:700;font-size:21px;letter-spacing:4px;color:var(--blue)}
.marker{left:592px;width:16px}

/* about */
.about{top:700px;height:555px}
.about-text{left:98px;top:205px;width:590px;font-size:15px;line-height:25px;color:#555}
.about-text p+p{margin-top:22px}
.btn-fill{background:var(--blue);color:#fff;border-radius:20px;font-family:"Montserrat",sans-serif;font-size:12px;font-weight:600;display:flex;align-items:center;justify-content:center}
.about-device{left:735px;top:195px;width:375px;height:310px;background:linear-gradient(135deg,#2b5fa8,#7fb3e6 50%,#d8dadc);border-radius:6px}

/* stats */
.stats{top:1255px;height:345px;background:linear-gradient(160deg,#5a5d61,#303336 60%,#26282b);clip-path:polygon(0 0,100% 0,100% 86%,50% 100%,0 86%)}
.stat{width:200px;text-align:center;color:#fff}
.stat svg{display:block;margin:0 auto 14px}
.stat b{display:block;font-family:"Montserrat",sans-serif;font-size:46px;font-weight:700;line-height:50px}
.stat span{font-family:"Montserrat",sans-serif;font-size:15px;letter-spacing:1px}

/* services */
.services{top:1600px;height:927px;background:var(--light);z-index:-1}
.card{width:277px;height:190px;background:#fff;border:1px solid #e2e2e2;text-align:center}
.card .ico{width:64px;height:64px;border-radius:50%;background:#dedede;margin:38px auto 18px;display:flex;align-items:center;justify-content:center}
.card p{font-family:"Montserrat",sans-serif;font-size:13px;line-height:18px;color:#555;font-weight:600}
.card.active{border:2px solid var(--blue)}
.card.active .ico{background:var(--blue)}
.card.active p{color:var(--blue)}

/* video */
.video{top:2527px;height:358px;background:linear-gradient(135deg,#1a1c1f,#4a4d51 50%,#1a1c1f)}
.video h2{top:88px;font-family:"Montserrat",sans-serif;font-size:42px;font-weight:800;color:var(--blue)}
.video .lead{top:140px;color:#fff;font-size:14px;font-style:italic}
.video .play{left:564px;top:170px}
.video .dur{top:258px;color:#fff;font-size:13px;font-style:italic}

/* different */
.different{top:2885px;height:652px}
.portrait{left:0;top:0;width:650px;height:652px;background:linear-gradient(90deg,#c9ccd0,#e6e8ea 60%,rgba(255,255,255,0))}
.different .ghost{color:rgba(255,255,255,.75)}
.accordion{left:508px;top:170px;width:594px}
.acc-head{height:70px;border:1px solid #ddd;background:#fff;display:flex;align-items:center;justify-content:space-between;padding:0 26px 0 0;font-family:"Montserrat",sans-serif;font-size:16px;font-weight:600;margin-bottom:5px}
.acc-head span:first-child{flex:1;text-align:center}
.acc-head.open{background:var(--blue);color:#fff;border-color:var(--blue)}
.acc-body{text-align:center;font-size:15px;line-height:24px;color:#444;padding:14px 40px 20px}

/* team */
.team{top:3537px;height:538px}
.member{width:235px;height:294px;background:#fff;border:1px solid #ddd;box-shadow:0 2px 6px rgba(0,0,0,.08);text-align:center}
.member .photo{width:98px;height:98px;border-radius:50%;border:4px solid var(--blue);background:linear-gradient(160deg,#cfd6dd,#8b96a3);margin:22px auto 10px}
.member .role{font-size:9px;color:#888;letter-spacing:1px}
.member .name{font-family:"Montserrat",sans-serif;font-weight:700;font-size:15px;color:var(--blue);margin:3px 0 8px}
.member .bio{font-size:10px;line-height:14px;color:#666;padding:0 14px}
.member .mail{font-size:10px;color:#555;margin:8px 0 7px}
.member .dots{display:flex;gap:5px;justify-content:center}
.member .dots i{width:20px;height:20px;border-radius:50%;background:var(--blue);display:block}
.pager{top:500px;display:flex;gap:10px;justify-content:center}
.pager i{width:8px;height:8px;border-radius:50%;background:#bbb;display:block}
.pager i.on{background:var(--blue)}

/* works */
.works{top:4075px;height:522px;background:var(--blue)}
.works .ghost{color:rgba(255,255,255,.3)}
.works .sub{color:#fff}
.work{top:170px;height:286px}
.work-strip{top:456px;height:66px;left:0;width:1200px;background:var(--navy)}

/* contact */
.contact{top:4597px;height:254px;background:#eceff1}
.chev{left:0;top:0}
.contact-col{width:300px;text-align:center;font-size:15px;line-height:22px;color:#444}
.contact-col svg{display:block;margin:0 auto 14px}
.contact-col .rule{width:30px;height:2px;background:#555;margin:16px auto 0}
.footer{top:4851px;height:40px;background:var(--navy);color:#ccc;font-size:12px;display:flex;align-items:center;justify-content:center}
</style>
</head>
<body>

<header class="section hero">
  <div class="hero-photo" role="img" aria-label="Dark photo of a laptop on a desk seen from the front"></div>
  <div class="abs site-logo"><span class="mark"></span><span class="word">BrightAndSteady.example<small>WEB DESIGN &amp; MARKETING</small></span></div>
  <nav class="abs nav"><span class="active">HOME</span><span>SERVICES &amp; PRICING</span><span>OUR TEAM</span><span>CLIENTS/PORTFOLIO</span><span>CONTACT US</span></nav>
  <div class="abs phone-btn"><svg width="20" height="20" viewBox="0 0 24 24"><path fill="#fff" d="M6.6 10.8a15 15 0 0 0 6.6 6.6l2.2-2.2a1 1 0 0 1 1-.25 11.4 11.4 0 0 0 3.6.57 1 1 0 0 1 1 1V20a1 1 0 0 1-1 1A17 17 0 0 1 3 4a1 1 0 0 1 1-1h3.5a1 1 0 0 1 1 1c0 1.25.2 2.45.57 3.6a1 1 0 0 1-.25 1z"/></svg>01-55501234</div>
  <div class="abs center hero-kicker">THE DESIGN &amp; MARKETING TEAM</div>
  <h1 class="abs center hero-title">THAT ALWAYS PUTS TRUST &amp;<br>LOYALTY BEFORE PROFITS</h1>
  <svg class="abs hero-swoosh" width="90" height="22" viewBox="0 0 90 22"><path d="M2 18 Q45 2 88 6" stroke="#fff" stroke-width="3" fill="none" stroke-linecap="round"/></svg>
  <div class="abs btn-outline">MORE ABOUT US</div>
  <div class="abs center scroll">SCROLL DOWN</div>
</header>

<section class="section about">
  <div class="abs center ghost" style="top:80px">ABOUT US</div>
  <div class="abs center sub" style="top:118px">ABOUT US</div>
  <svg class="abs marker" style="top:150px" width="16" height="30" viewBox="0 0 16 30"><line x1="8" y1="0" x2="8" y2="18" stroke="#1ea7e1" stroke-width="2"/><circle cx="8" cy="23" r="5" fill="none" stroke="#1ea7e1" stroke-width="2"/></svg>
  <div class="abs about-text">
    <p>We believe that honesty and integrity come before personal profits. We are a family owned and operated company. Our parents raised us to take care of each other and that's exactly what we've done. We treat each of our clients with the same loyalty and respect that we give each other.</p>
    <p>We are not looking to have hundreds and hundreds of clients. We are looking to expand our family with a handful of like-minded individuals. Companies who take pride in their work and their customers. We want to build mutually beneficial, lucrative, and long term partnerships.</p>
  </div>
  <div class="abs btn-fill" style="left:98px;top:462px;width:120px;height:38px">READ MORE</div>
  <div class="abs about-device" role="img" aria-label="Photo of a laptop and a smartphone showing a blue digital screen"></div>
</section>

<section class="section stats" role="img" aria-label="Desk photo background with phone, keyboard and earphones">
  <div class="abs stat" style="left:216px;top:90px"><svg width="44" height="48" viewBox="0 0 44 48"><rect x="6" y="2" width="32" height="44" rx="3" fill="none" stroke="#fff" stroke-width="3"/><path d="M13 14h18M13 22h18M13 30h12" stroke="#fff" stroke-width="3"/></svg><b>561</b><span>PROJECTS DELIVERED</span></div>
  <div class="abs stat" style="left:422px;top:90px"><svg width="44" height="48" viewBox="0 0 44 48"><path d="M10 4h24v12a12 12 0 0 1-24 0z" fill="none" stroke="#fff" stroke-width="3"/><path d="M10 8H3a7 7 0 0 0 7 10M34 8h7a7 7 0 0 1-7 10M22 28v10M12 44h20" stroke="#fff" stroke-width="3" fill="none"/></svg><b>24</b><span>AWARDS WON</span></div>
  <div class="abs stat" style="left:607px;top:90px"><svg width="48" height="48" viewBox="0 0 48 48"><path d="M4 22h9v22H4zM13 42h22a4 4 0 0 0 4-3l4-14a4 4 0 0 0-4-5H28l2-10a4 4 0 0 0-7-3L13 22" fill="none" stroke="#fff" stroke-width="3" stroke-linejoin="round"/></svg><b>160</b><span>HAPPY CLIENTS</span></div>
  <div class="abs stat" style="left:816px;top:90px"><svg width="44" height="48" viewBox="0 0 44 48"><circle cx="22" cy="14" r="9" fill="none" stroke="#fff" stroke-width="3"/><path d="M4 46a18 18 0 0 1 36 0z" fill="none" stroke="#fff" stroke-width="3"/></svg><b>285</b><span>EMPLOYEES WORKING</span></div>
</section>

<section class="section services">
  <div class="abs center ghost" style="top:82px">SERVICES &amp; PRICING</div>
  <div class="abs center sub" style="top:138px">SERVICES &amp; PRICING</div>
  <svg class="abs marker" style="top:168px" width="16" height="30" viewBox="0 0 16 30"><line x1="8" y1="0" x2="8" y2="18" stroke="#1ea7e1" stroke-width="2"/><circle cx="8" cy="23" r="5" fill="none" stroke="#1ea7e1" stroke-width="2"/></svg>

  <div class="abs card" style="left:98px;top:216px"><div class="ico"><svg width="30" height="30" viewBox="0 0 30 30"><rect x="3" y="5" width="24" height="20" fill="none" stroke="#555" stroke-width="2"/><path d="M3 10h24M7 14h8v7H7zM18 14h6M18 18h6" stroke="#555" stroke-width="2" fill="none"/></svg></div><p>WEBSITE DESIGN<br>&amp; MANAGEMENT</p></div>
  <div class="abs card active" style="left:456px;top:216px"><div class="ico"><svg width="30" height="30" viewBox="0 0 30 30"><path d="M5 25 25 5M5 5l20 20" stroke="#fff" stroke-width="3" stroke-linecap="round"/></svg></div><p>LOGO DESIGN &amp;<br>BRANDING MATERIALS</p></div>
  <div class="abs card" style="left:821px;top:216px"><div class="ico"><svg width="30" height="30" viewBox="0 0 30 30"><path d="M2 4h5l3 15h15l3-10H9" fill="none" stroke="#555" stroke-width="2"/><circle cx="12" cy="24" r="2" fill="#555"/><circle cx="23" cy="24" r="2" fill="#555"/></svg></div><p>ONLINE STORE DESIGN<br>&amp; MANAGEMENT</p></div>

  <div class="abs card" style="left:98px;top:437px"><div class="ico"><svg width="30" height="30" viewBox="0 0 30 30"><path d="M15 28s-9-9-9-16a9 9 0 0 1 18 0c0 7-9 16-9 16z" fill="none" stroke="#555" stroke-width="2"/><circle cx="15" cy="12" r="3" fill="#555"/></svg></div><p>LOCAL SEO<br>MANAGEMENT</p></div>
  <div class="abs card" style="left:456px;top:437px"><div class="ico"><svg width="30" height="30" viewBox="0 0 30 30"><circle cx="12" cy="12" r="8" fill="none" stroke="#555" stroke-width="2"/><path d="M18 18l9 9" stroke="#555" stroke-width="3"/></svg></div><p>SEARCH ENGINE<br>OPTIMIZATION</p></div>
  <div class="abs card" style="left:821px;top:437px"><div class="ico"><svg width="30" height="30" viewBox="0 0 30 30"><path d="M4 12h6l12-7v20l-12-7H4zM8 18l2 8" fill="none" stroke="#555" stroke-width="2" stroke-linejoin="round"/></svg></div><p>SOCIAL MEDIA<br>MARKETING</p></div>

  <div class="abs card" style="left:98px;top:672px"><div class="ico"><svg width="30" height="30" viewBox="0 0 30 30"><circle cx="15" cy="15" r="11" fill="none" stroke="#555" stroke-width="2"/><circle cx="15" cy="15" r="4" fill="#555"/></svg></div><p>MARKETING MATERIAL<br>&amp; PRINT DESIGN</p></div>
  <div class="abs card" style="left:456px;top:672px"><div class="ico"><svg width="30" height="30" viewBox="0 0 30 30"><circle cx="15" cy="15" r="4" fill="#555"/><path d="M15 2v8M15 20v8M2 15h8M20 15h8M6 6l5 5M19 19l5 5M24 6l-5 5M11 19l-5 5" stroke="#555" stroke-width="2"/></svg></div><p>OUTSOURCING<br>MANAGEMENT</p></div>
  <div class="abs card" style="left:821px;top:672px"><div class="ico"><svg width="30" height="30" viewBox="0 0 30 30"><circle cx="9" cy="9" r="4" fill="none" stroke="#555" stroke-width="2"/><circle cx="21" cy="9" r="4" fill="none" stroke="#555" stroke-width="2"/><path d="M2 26a7 7 0 0 1 14 0M14 26a7 7 0 0 1 14 0" fill="none" stroke="#555" stroke-width="2"/></svg></div><p>CONSULTING</p></div>
</section>

<section class="section video" role="img" aria-label="Dark background photo of tall city buildings">
  <h2 class="abs center">WATCH OUR INTRO VIDEO</h2>
  <div class="abs center lead">Lorem ipsum dolor sit amet consectetur elit</div>
  <svg class="abs play" width="72" height="72" viewBox="0 0 72 72"><circle cx="36" cy="36" r="33" fill="none" stroke="#fff" stroke-width="3"/><path d="M29 22v28l22-14z" fill="none" stroke="#fff" stroke-width="3" stroke-linejoin="round"/></svg>
  <div class="abs center dur">Duration : 3 : 44</div>
</section>

<section class="section different">
  <div class="abs portrait" role="img" aria-label="Faded photo of a thoughtful businessman"></div>
  <div class="abs center ghost" style="top:36px">WHAT MAKES ME DIFFERENT?</div>
  <div class="abs center sub" style="top:92px">WHAT MAKES ME DIFFERENT?</div>
  <svg class="abs marker" style="top:122px" width="16" height="30" viewBox="0 0 16 30"><line x1="8" y1="0" x2="8" y2="18" stroke="#1ea7e1" stroke-width="2"/><circle cx="8" cy="23" r="5" fill="none" stroke="#1ea7e1" stroke-width="2"/></svg>
  <div class="abs accordion">
    <div class="acc-head open"><span>100% RISK FREE INVESTMENT</span><span>&minus;</span></div>
    <div class="acc-body">If we are unable to deliver anything that we say we can we will refund you 100% of your investment.</div>
    <div class="acc-head"><span>CUSTOMER LOYALTY PROGRAM</span><span>+</span></div>
    <div class="acc-head"><span>24/7 U.S. BASED CUSTOMER SUPPORT</span><span>+</span></div>
    <div class="acc-head"><span>UNMATCHED PERSONAL SERVICE</span><span>+</span></div>
    <div class="acc-head"><span>MULTIPLE PAYMENT OPTIONS AVAILABLE</span><span>+</span></div>
  </div>
</section>

<section class="section team">
  <div class="abs center ghost" style="top:38px">MY TEAM</div>
  <div class="abs center sub" style="top:96px">MY TEAM</div>
  <svg class="abs marker" style="top:126px" width="16" height="30" viewBox="0 0 16 30"><line x1="8" y1="0" x2="8" y2="18" stroke="#1ea7e1" stroke-width="2"/><circle cx="8" cy="23" r="5" fill="none" stroke="#1ea7e1" stroke-width="2"/></svg>

  <div class="abs member" style="left:98px;top:180px"><div class="photo" role="img" aria-label="Team member portrait"></div><div class="role">CHIEF EXECUTIVE OFFICER</div><div class="name">CLIENT NAME</div><p class="bio">Our founder guides every project from first call to launch, keeping each client close and every promise kept.</p><div class="mail">Email: team@brightandsteady.example</div><div class="dots"><i></i><i></i><i></i></div></div>
  <div class="abs member" style="left:349px;top:180px"><div class="photo" role="img" aria-label="Team member portrait"></div><div class="role">CHIEF DESIGN OFFICER</div><div class="name">CLIENT NAME</div><p class="bio">Leads our design studio, shaping logos, websites and print pieces that feel clear, friendly and true to you.</p><div class="mail">Email: team@brightandsteady.example</div><div class="dots"><i></i><i></i><i></i></div></div>
  <div class="abs member" style="left:600px;top:180px"><div class="photo" role="img" aria-label="Team member portrait"></div><div class="role">CHIEF TECHNICAL OFFICER</div><div class="name">CLIENT NAME</div><p class="bio">Builds fast, secure sites and keeps them running smoothly so your business stays online every single day.</p><div class="mail">Email: team@brightandsteady.example</div><div class="dots"><i></i><i></i><i></i></div></div>
  <div class="abs member" style="left:854px;top:180px"><div class="photo" role="img" aria-label="Team member portrait"></div><div class="role">FINANCE</div><div class="name">CLIENT NAME</div><p class="bio">Keeps our pricing honest and simple, helping every client plan a budget that grows along with their goals.</p><div class="mail">Email: team@brightandsteady.example</div><div class="dots"><i></i><i></i><i></i></div></div>

  <div class="abs center pager"><i class="on"></i><i></i><i></i></div>
</section>

<section class="section works">
  <div class="abs center ghost" style="top:40px">LATEST WORKS</div>
  <div class="abs center sub" style="top:96px;color:#fff">LATEST WORKS</div>
  <svg class="abs marker" style="top:126px" width="16" height="30" viewBox="0 0 16 30"><line x1="8" y1="0" x2="8" y2="18" stroke="#fff" stroke-width="2"/><circle cx="8" cy="23" r="5" fill="none" stroke="#fff" stroke-width="2"/></svg>
  <div class="abs work" style="left:0;width:290px;background:linear-gradient(135deg,#111,#2a2d31)" role="img" aria-label="Portfolio sample: dark business card design"></div>
  <div class="abs work" style="left:300px;width:290px;background:linear-gradient(135deg,#d8cfc4,#f1ece6)" role="img" aria-label="Portfolio sample: person working on a laptop"></div>
  <div class="abs work" style="left:600px;width:290px;background:linear-gradient(135deg,#8b7560,#cfc7bd)" role="img" aria-label="Portfolio sample: laptop on a wooden desk"></div>
  <div class="abs work" style="left:900px;width:300px;background:linear-gradient(135deg,#3b3f44,#bfc6cc)" role="img" aria-label="Portfolio sample: website shown on a monitor"></div>
  <div class="abs work-strip">
    <svg class="abs" style="left:548px;top:26px" width="104" height="14" viewBox="0 0 104 14"><path d="M8 2 2 7l6 5" stroke="#fff" stroke-width="2" fill="none"/><circle cx="34" cy="7" r="4" fill="#1ea7e1"/><circle cx="52" cy="7" r="4" fill="#fff"/><circle cx="70" cy="7" r="4" fill="#fff"/><path d="m96 2 6 5-6 5" stroke="#fff" stroke-width="2" fill="none"/></svg>
  </div>
</section>

<section class="section contact">
  <svg class="abs chev" width="1200" height="254" viewBox="0 0 1200 254"><path d="M0 0h360l40 127-40 127H0z" fill="#f6f7f8"/><path d="M400 0h360l40 127-40 127H400l40-127z" fill="#e6e9ec"/><path d="M800 0h400v254H800l40-127z" fill="#f6f7f8"/></svg>
  <div class="abs contact-col" style="left:52px;top:40px"><svg width="44" height="52" viewBox="0 0 44 52"><path d="M22 50S6 32 6 20a16 16 0 0 1 32 0c0 12-16 30-16 30z" fill="none" stroke="#1ea7e1" stroke-width="3"/><circle cx="22" cy="20" r="6" fill="none" stroke="#1ea7e1" stroke-width="3"/></svg>Address Goes Here<br>text of the printing and<br>typesetting industry.<div class="rule"></div></div>
  <div class="abs contact-col" style="left:450px;top:40px"><svg width="50" height="52" viewBox="0 0 24 24"><path fill="none" stroke="#1ea7e1" stroke-width="1.4" d="M6.6 10.8a15 15 0 0 0 6.6 6.6l2.2-2.2a1 1 0 0 1 1-.25 11.4 11.4 0 0 0 3.6.57 1 1 0 0 1 1 1V20a1 1 0 0 1-1 1A17 17 0 0 1 3 4a1 1 0 0 1 1-1h3.5a1 1 0 0 1 1 1c0 1.25.2 2.45.57 3.6a1 1 0 0 1-.25 1z"/></svg>+01 555 0190 - Office<br>(01) 555 0191 - Fax<div class="rule"></div></div>
  <div class="abs contact-col" style="left:854px;top:40px"><svg width="52" height="52" viewBox="0 0 52 52"><path d="M4 24 48 4 40 46 26 34l-8 12V30L48 4" fill="none" stroke="#1ea7e1" stroke-width="3" stroke-linejoin="round"/></svg>support@brightandsteady.example<br>info@brightandsteady.example<div class="rule"></div></div>
</section>

<footer class="section footer">&copy;2017 Bright And Steady Web Design &amp; Marketing | All Rights Reserved</footer>

</body>
</html>
```